Employment Agency Website Design

We are working with an employment agency in California.

Some sites to use for content/competitors and inspiration:

https://www.travinmoor.example/us/en
https://www.pelkoworksusa.example
https://www.dunmarhire.example
https://www.vantriga.example/en
https://www.ombrelusa.example
https://www.quilnstaffing.example

Thank you for taking the time to consider designing a website for us. We are web developers based in Stockton, CA, USA. Most of our projects go through the same process. Understanding this process may help you win a project with us. We custom-code all of our websites in-house. We don’t have any requirements as to what tools you use for your design, but we prefer Figma files. For any design that we label as four-stars, we send it to the client for review. The client picks the final design they want us to use. Once we complete this process, we will continue to show additional clients all the four-star sites and purchase them later. Your designs will have multiple chances to sell. For better chances of success, we ask that you follow these guidelines.

IMAGES:
If you use any images or icons in the design, we ask that you have a link to the asset so we can purchase the image/icon. Most of the designs we submit do not have the customer’s images on them unless they have some great images. Be creative; show us the feeling you are trying to portray with your image choices. Use any royalty-free site you choose. We subscribe to Adobe and mainly use their images, but we can purchase images outside of Adobe. PLEASE NOTE: we will not submit designs to clients with watermarks on the images.

FONTS:
We ask that you identify the fonts used in the design. This can be done in a message if you want. We typically use Google Fonts and Adobe Fonts.

CONTENT:
We're always open to different content and ideas. We often submit designs with stock images so the client can see our vision. We typically take pictures after the website launch to use their images with our vision. Lorem Ipsum is fine for paragraphs, but we ask that you write the headers in correct English. We want to be able to show the vision and identify the sections of the website.

INSPIRATION:
We typically add a couple of links in the brief of websites we like to help you get started in your design.

REVISIONS:
We do not often ask for revisions of the designs unless we see something in the design that may not appeal to the client. If there are slight changes that we want to make, we do that in the development process.

FEEDBACK:
We rarely give feedback on designs during the design process. We are working on many website projects and do not have the time to provide feedback. We usually respond if your request is well thought out and asks specific questions, but a note asking “feedback, please” usually goes unanswered.

```html
<!DOCTYPE html>
<html lang="en">
<head>
<meta charset="utf-8">
<title>Kestrelwork — Helping Good People Find Good Jobs</title>
<link href="https://fonts.googleapis.com/css2?family=Montserrat:wght@700;800&family=Nunito+Sans:ital,wght@0,300;0,400;0,600;0,700;0,800;1,400&display=swap" rel="stylesheet">
<style>
:root{
  --red:#be1e2d;
  --pink:#fcdde3;
  --pink-soft:#fbe6ea;
  --ink:#1b1b1b;
  --muted:#7a6f72;
  --white:#ffffff;
  --black:#0b0b0d;
}
*{margin:0;padding:0;box-sizing:border-box}
html,body{width:1200px;height:4946px;overflow:hidden}
body{position:relative;background:var(--white);font-family:"Nunito Sans",sans-serif;color:var(--ink)}
.abs{position:absolute}
.btn{position:absolute;display:flex;align-items:center;justify-content:center;font-weight:800;text-transform:uppercase;color:var(--white);text-decoration:none}
.btn-red{background:var(--red)}
.btn-dark{background:var(--ink)}
.para{color:var(--muted);font-weight:300;font-size:15px;line-height:20px}
.ph{position:absolute}

/* hero */
.hero{position:absolute;left:0;top:0;width:1200px;height:662px;background:var(--pink);overflow:hidden}
.hero-sheen{position:absolute;inset:0;background:linear-gradient(160deg,transparent 45%,#f8d3db 45.2%,#fae0e6 70%)}
.topbar{position:absolute;left:688px;top:0;width:512px;height:40px;background:var(--red);clip-path:polygon(22px 0,100% 0,100% 100%,0 100%);display:flex;align-items:center;justify-content:flex-end;gap:34px;padding-right:32px;color:var(--white);font-size:15px}
.topbar span{display:flex;align-items:center;gap:8px}
.brand{position:absolute;display:flex;align-items:center;gap:10px}
.brand-mark{width:30px;height:30px;border-radius:50%;background:var(--red)}
.brand-name{font-weight:700;font-size:30px;color:var(--red)}
.tagline{position:absolute;left:90px;top:70px;font-size:12px;color:var(--muted)}
.nav{position:absolute;top:52px;left:512px;display:flex;gap:58px;font-size:16px;color:var(--ink)}
.hero-title{position:absolute;left:48px;top:186px;font-family:"Montserrat",sans-serif;font-weight:800;font-size:61px;line-height:78px;color:var(--ink)}
.hero-photo{left:600px;top:40px;width:590px;height:622px;background:radial-gradient(ellipse at 55% 45%,#f4c4b4 0,#eeb9aa 28%,#f7d6dd 60%,transparent 75%)}

/* about */
.hex{left:80px;top:774px;width:435px;height:461px;clip-path:polygon(50% 0,100% 25%,100% 75%,50% 100%,0 75%,0 25%);background:linear-gradient(135deg,#4d5560,#2e3138 45%,#b7a79b)}
.badge{position:absolute;left:303px;top:1087px;width:294px;height:102px;background:var(--red);color:var(--white);display:flex;align-items:center;gap:14px;padding-left:18px}
.badge b{font-family:"Montserrat",sans-serif;font-size:68px;font-weight:700}
.badge span{font-size:23px;line-height:29px}
.h2{position:absolute;font-weight:800;color:var(--ink)}

/* services */
.services{position:absolute;left:0;top:1373px;width:1200px;height:393px;background:var(--pink)}
.service{position:absolute;top:0;width:340px;text-align:center}
.service svg{display:block;margin:57px auto 0}
.service h3{margin-top:22px;font-size:33px;font-weight:600}
.service p{margin-top:14px}

/* specialized */
.tag{position:absolute;width:230px;height:47px;border:3px solid var(--red);display:flex;align-items:center;justify-content:center;color:var(--red);font-weight:700;font-size:16px}
.learn{position:absolute;left:74px;top:2288px;color:var(--red);font-weight:800;font-size:15px;border-bottom:2px solid var(--red);padding-bottom:6px;width:126px}

/* how */
.how{position:absolute;left:0;top:2387px;width:1200px;height:474px;background:var(--pink)}
.step{position:absolute;top:0;width:340px}
.step .num{position:relative;height:136px;margin-top:147px}
.step .num i{position:absolute;left:0;top:36px;width:102px;height:102px;border-radius:50%;background:var(--red)}
.step .num b{position:absolute;left:12px;top:-22px;font-family:"Montserrat",sans-serif;font-weight:800;font-size:150px;line-height:1;color:var(--ink)}
.step h4{margin-top:38px;font-size:22px;font-weight:600}
.step p{margin-top:10px}

/* stories */
.story{position:absolute;width:496px;height:237px;background:var(--white);box-shadow:0 6px 30px rgba(190,30,45,.09);padding:44px 24px 0}
.story h5{font-size:22px;font-weight:600}
.story p{margin-top:10px;font-style:italic;font-size:23px;line-height:31px;color:var(--muted)}
.story small{display:block;margin-top:8px;color:var(--red);font-size:16px;font-weight:600}
.story svg{position:absolute;right:22px;top:26px}

/* subscribe */
.subscribe{position:absolute;left:0;top:3469px;width:1200px;height:275px;background:var(--pink)}
.field{position:absolute;left:722px;top:64px;width:397px;height:59px;background:var(--white);border:1px solid #f0c8d0;display:flex;align-items:center;padding-left:30px;font-size:17px;color:var(--muted)}

/* blog */
.post{position:absolute;top:3911px;width:320px;text-align:center}
.post .thumb{position:relative;height:254px;background:linear-gradient(160deg,#d9d9de,#8d8f99 55%,#43464f)}
.post .label{position:absolute;left:14px;top:0;background:var(--red);color:var(--white);font-weight:700;font-size:19px;padding:4px 22px}
.post .meta{margin-top:28px;font-size:12px;color:var(--muted)}
.post h6{margin-top:14px;font-size:16px;font-weight:800;line-height:20px}
.post p{margin-top:16px;font-size:11.5px;line-height:19px;color:var(--muted)}

/* cta */
.cta{position:absolute;left:0;top:4387px;width:1200px;height:231px;background:var(--pink)}

/* footer */
.footer{position:absolute;left:0;top:4618px;width:1200px;height:328px;background:var(--black);color:var(--white)}
.fcol{position:absolute;top:90px}
.fcol h6{font-size:17px;font-weight:800;letter-spacing:.5px}
.fcol ul{list-style:none;margin-top:16px;font-size:13px;line-height:29px}
.social{position:absolute;left:100px;top:172px;display:flex;gap:26px}
.social i{width:14px;height:14px;border-radius:50%;background:var(--white)}
</style>
</head>
<body>

<section class="hero">
  <div class="hero-sheen"></div>
  <div class="ph hero-photo" role="img" aria-label="Smiling young woman holding a laptop and glasses"></div>
  <div class="topbar">
    <span><svg width="18" height="18" viewBox="0 0 18 18"><circle cx="9" cy="9" r="9" fill="#fff"/><circle cx="9" cy="7" r="3" fill="#be1e2d"/><path d="M3.5 14.5a6 4 0 0 1 11 0" fill="#be1e2d"/></svg>Client Login</span>
    <span><svg width="18" height="18" viewBox="0 0 18 18"><circle cx="9" cy="9" r="9" fill="#fff"/><circle cx="9" cy="7" r="3" fill="#be1e2d"/><path d="M3.5 14.5a6 4 0 0 1 11 0" fill="#be1e2d"/></svg>Candidate Login</span>
  </div>
  <div class="brand" style="left:44px;top:30px"><i class="brand-mark"></i><span class="brand-name">Kestrelwork</span></div>
  <div class="tagline">The future of work.</div>
  <nav class="nav"><span>Talent Seeker</span><span>Employers</span><span>Soltutions</span><span>About Us</span><span>Contact</span></nav>
  <h1 class="hero-title">Helping Good<br>People Find<br>Good Jobs</h1>
  <p class="para abs" style="left:56px;top:430px;width:430px">Lorem ipsum dolor sit amet, consectetuer adipiscing elit. Aenean commodo ligula eget dolor. Aenean massa.</p>
  <a class="btn btn-red" style="left:56px;top:495px;width:198px;height:43px;font-size:13px">Find Your Next Job</a>
  <a class="btn btn-dark" style="left:278px;top:495px;width:198px;height:43px;font-size:13px">Find Your Next Hire</a>
</section>

<section>
  <div class="ph hex" role="img" aria-label="Smiling businessman shaking hands in an office"></div>
  <div class="badge"><b>10+</b><span>Years of<br>Experience</span></div>
  <h2 class="h2" style="left:649px;top:868px;font-size:47px">About Us</h2>
  <p class="para abs" style="left:649px;top:944px;width:480px">Lorem ipsum dolor sit amet, consectetuer adipiscing elit. Aenean commodo ligula eget dolor. Aenean massa. Cum sociis natoque penatibus et magnis dis parturient montes, nascetur ridiculus mus.</p>
  <p class="para abs" style="left:649px;top:1024px;width:480px">Donec quam felis, ultricies nec, pellentesque eu, pretium quis, sem. Nulla consequat massa quis enim. Donec pede justo, fringilla vel, aliquet nec, vulputate eget, arcu.</p>
  <a class="btn btn-red" style="left:649px;top:1112px;width:198px;height:37px;font-size:13px">Find Your Next Job</a>
</section>

<section class="services">
  <div class="service" style="left:34px">
    <svg width="130" height="125" viewBox="0 0 130 125" fill="none" stroke="#be1e2d" stroke-width="4"><rect x="30" y="4" width="80" height="110" rx="4"/><path d="M70 36h28M70 50h28M70 64h28M46 96h52"/><circle cx="40" cy="70" r="26"/><path d="M58 88l20 22"/></svg>
    <h3>Recruitment</h3>
    <p class="para">Lorem ipsum dolor sit amet, consectetur<br>adipiscing elit, sed do eiusmod<br>tempor incididunt.</p>
  </div>
  <div class="service" style="left:420px">
    <svg width="150" height="125" viewBox="0 0 150 125" fill="none" stroke="#be1e2d" stroke-width="4"><rect x="6" y="28" width="110" height="82" rx="6"/><path d="M42 28V12h38v16M6 60h110"/><circle cx="108" cy="70" r="24" fill="#fcdde3"/><path d="M124 88l18 20"/></svg>
    <h3>Certified Methods</h3>
    <p class="para">Lorem ipsum dolor sit amet, consectetur<br>adipiscing elit, sed do eiusmod<br>tempor incididunt.</p>
  </div>
  <div class="service" style="left:825px">
    <svg width="150" height="125" viewBox="0 0 150 125" role="img" aria-label="Handshake icon"><rect x="20" y="40" width="110" height="70" rx="30" fill="#f3b7c2"/></svg>
    <h3>Expatriate Services</h3>
    <p class="para">Lorem ipsum dolor sit amet, consectetur<br>adipiscing elit, sed do eiusmod<br>tempor incididunt.</p>
  </div>
</section>

<section>
  <h2 class="h2" style="left:74px;top:1905px;font-size:36px;line-height:46px">Specialized Talent Across<br>&nbsp;Your Organization</h2>
  <div class="tag" style="left:71px;top:2047px">Finance and Accounting</div>
  <div class="tag" style="left:330px;top:2047px">Government</div>
  <div class="tag" style="left:71px;top:2116px">Technology</div>
  <div class="tag" style="left:330px;top:2116px">Marketing &amp; Creative</div>
  <div class="tag" style="left:71px;top:2187px">Legal</div>
  <div class="tag" style="left:330px;top:2187px">Customer Support</div>
  <span class="learn">Learn More</span>
</section>

<section class="how">
  <h2 class="h2" style="left:0;width:1180px;text-align:center;top:65px;font-size:35px">How It Works</h2>
  <div class="step" style="left:71px"><div class="num"><i></i><b>1</b></div><h4>Describe Your Need</h4><p class="para">Lorem ipsum dolor sit amet, consectetur<br>adipiscing elit, sed do eiusmod<br>tempor incididunt.</p></div>
  <div class="step" style="left:461px"><div class="num"><i></i><b>2</b></div><h4>Describe Your Need</h4><p class="para">Lorem ipsum dolor sit amet, consectetur<br>adipiscing elit, sed do eiusmod<br>tempor incididunt.</p></div>
  <div class="step" style="left:858px"><div class="num"><i></i><b>3</b></div><h4>Describe Your Need</h4><p class="para">Lorem ipsum dolor sit amet, consectetur<br>adipiscing elit, sed do eiusmod<br>tempor incididunt.</p></div>
</section>
<div class="ph" style="left:705px;top:1795px;width:235px;height:672px;background:linear-gradient(180deg,#e8d3c8 0,#f2f2f2 18%,#eaeaea 45%,#1f1f22 58%,#111 100%);border-radius:90px 90px 30px 30px" role="img" aria-label="Young professional in white shirt and tie carrying a briefcase"></div>

<section>
  <h2 class="h2" style="left:0;width:1195px;text-align:center;top:2966px;font-size:35px">Success Stories</h2>
  <div class="story" style="left:67px;top:3085px">
    <svg width="60" height="50" viewBox="0 0 60 50" fill="#be1e2d"><path d="M0 0h26v26l-12 24H4l8-22H0zM32 0h26v26l-12 24H36l8-22H32z"/></svg>
    <h5>Mara Ellison</h5><p>Lorem ipsum dolor sit amet, consectetur adipiscing elit, sed do eiusmod tempor incididunt.</p><small>Sales assistant</small>
  </div>
  <div class="story" style="left:624px;top:3082px">
    <svg width="60" height="50" viewBox="0 0 60 50" fill="#be1e2d"><path d="M0 0h26v26l-12 24H4l8-22H0zM32 0h26v26l-12 24H36l8-22H32z"/></svg>
    <h5>Mara Ellison</h5><p>Lorem ipsum dolor sit amet, consectetur adipiscing elit, sed do eiusmod tempor incididunt.</p><small>Sales assistant</small>
  </div>
</section>

<section class="subscribe">
  <h2 class="h2" style="left:83px;top:94px;font-size:35px">Subscribe to Get Latest Updates</h2>
  <p class="para abs" style="left:93px;top:154px;width:520px;font-size:16px;line-height:23px">Lorem ipsum dolor sit amet, consectetur adipiscing elit, sed do eiusmod tempor incididunt.</p>
  <div class="field">Email Address</div>
  <a class="btn btn-red" style="left:722px;top:146px;width:397px;height:60px;font-size:21px;font-weight:700">Subscribe Now</a>
</section>

<section>
  <article class="post" style="left:100px">
    <div class="thumb" role="img" aria-label="Group of candidates waiting for interviews"><span class="label">Interview</span></div>
    <div class="meta">&#9679; rhea &nbsp;&nbsp; &#9632; August 24, 2023</div>
    <h6>The Power Of Networking In Your<br>Job Search</h6>
    <p>Cras semper pharetra dolor in sollicitudin. Vestibulum nunc risus, tempor ac ligula et, hendrerit vestibulum est. Interdum et malesuada fames...</p>
  </article>
  <article class="post" style="left:436px">
    <div class="thumb" role="img" aria-label="Applicants seated in a bright office hallway" style="background:linear-gradient(160deg,#f1f1f3,#b9bcc4 55%,#5a5e68)"><span class="label">Job Search Tips</span></div>
    <div class="meta">&#9679; rhea &nbsp;&nbsp; &#9632; August 24, 2023</div>
    <h6>Crafting A Winning Resume, Dos<br>And Don'ts</h6>
    <p>Cras semper pharetra dolor in sollicitudin. Vestibulum nunc risus, tempor ac ligula et, hendrerit vestibulum est. Interdum et malesuada fames...</p>
  </article>
  <article class="post" style="left:772px">
    <div class="thumb" role="img" aria-label="Recruiters reviewing a candidate at a table" style="background:linear-gradient(160deg,#dfe1e6,#7f8594 55%,#2f3340)"><span class="label">Job Search</span></div>
    <div class="meta">&#9679; rhea &nbsp;&nbsp; &#9632; August 24, 2023</div>
    <h6>Navigating Industry Trends In<br>Recruitment</h6>
    <p>Cras semper pharetra dolor in sollicitudin. Vestibulum nunc risus, tempor ac ligula et, hendrerit vestibulum est. Interdum et malesuada fames...</p>
  </article>
</section>

<section class="cta">
  <a class="btn btn-red" style="left:246px;top:85px;width:357px;height:69px;font-size:26px;font-weight:700">Find Your Next Job</a>
  <a class="btn btn-dark" style="left:645px;top:85px;width:357px;height:69px;font-size:26px;font-weight:700">Find Your Next Hire</a>
</section>

<footer class="footer">
  <div class="brand" style="left:100px;top:62px"><i class="brand-mark"></i><span class="brand-name" style="font-size:28px">Kestrelwork</span></div>
  <div class="abs" style="left:148px;top:102px;font-size:11px;color:#9a9a9a">The future of work.</div>
  <p class="abs" style="left:100px;top:124px;width:340px;font-size:12px;line-height:20px">Getting an accurate diagnosis can be one of the most impactful experiences that you can have.</p>
  <div class="social"><i></i><i></i><i></i><i></i></div>
  <div class="fcol" style="left:455px"><h6>QUICK LINKS</h6><ul><li>Home</li><li>About Us</li><li>Services</li><li>Contact</li></ul></div>
  <div class="fcol" style="left:659px"><h6>OTHER PAGES</h6><ul><li>Job Vacancy</li><li>Charity Program</li><li>Privacy &amp; Policy</li><li>Terms of Use</li></ul></div>
  <div class="fcol" style="left:862px;width:270px"><h6>CONTACT INFO</h6>
    <ul style="line-height:20px">
      <li style="display:flex;gap:12px;margin-bottom:12px"><svg width="12" height="16" viewBox="0 0 12 16"><path d="M6 0a6 6 0 0 1 6 6c0 4-6 10-6 10S0 10 0 6a6 6 0 0 1 6-6z" fill="#2ec4a6"/><circle cx="6" cy="6" r="2" fill="#0b0b0d"/></svg><span>418 Harbor Lane, Linden Bay,<br>CA 95290</span></li>
      <li style="display:flex;gap:12px;margin-bottom:12px"><svg width="13" height="13" viewBox="0 0 13 13"><path d="M2 0l3 3-2 2a8 8 0 0 0 5 5l2-2 3 3-2 2C5 13 0 8 0 2z" fill="#2ec4a6"/></svg>+1 209 555 0147</li>
      <li style="display:flex;gap:12px"><svg width="14" height="11" viewBox="0 0 14 11" fill="none" stroke="#2ec4a6" stroke-width="1.5"><rect x="1" y="1" width="12" height="9"/><path d="M1 1l6 5 6-5"/></svg>contact@kestrelwork.example</li>
    </ul>
  </div>
  <div class="abs" style="right:38px;top:296px;font-size:11px">Copyright © 2021. All rights reserved.</div>
</footer>

</body>
</html>
```